Carpentry company Needs a business card design

We need a design for a Carpentry / building company, business card. Please think of designs out of the ordinary and try to make it eye catching. Our existing logo will need to be incorporated in the design. However feel free to change the colours of the logo to suit your design. I would like to see some designs with green /black and orange incorporated into it.These are not the only colours accepted and all designs that appeal will be accepted.

Please contact me should you have any questions
Thanks Martin

Target Market(s)

General Public seeking carpentry work

Industry/Entity Type

Business

Contact Information for Business Card

- Current company logo ( colours can be changed)
-Phone number ,
- info@brelvanbuild.com.au
- brelvanbuild.com.au
-the facebook symbol

Font styles to use
Other font styles liked:
• You choose

Requirements
Must have
• Services we provide
• - Renovations
• -Deckings & Pergolas
• -Kitchens
• - Bathrooms
• - Intricate details
Nice to have
• an awesome design
Should not have
• Tools on the business card

```html
<!DOCTYPE html>
<html lang="en">
<head>
<meta charset="utf-8">
<title>Brelvan Build – Business Card</title>
<link rel="stylesheet" href="https://fonts.googleapis.com/css2?family=Open+Sans:wght@400;600;700&display=swap">
<style>
  :root {
    --backdrop: #3b3734;
    --card-black: #0d0d0d;
    --brand-green: #127a0c;
    --accent-green: #3fa02e;
    --text-white: #ffffff;
    --text-soft: #e6e6e6;
    --divider: #2e2e2e;
  }
  * { box-sizing: border-box; margin: 0; padding: 0; }
  html, body {
    width: 1200px; height: 900px; overflow: hidden;
    background: var(--backdrop);
    font-family: "Open Sans", Arial, sans-serif;
  }
  .canvas {
    position: relative; width: 1200px; height: 900px;
    display: flex; align-items: center; justify-content: center; gap: 60px;
  }
  .card {
    position: relative; width: 520px; height: 297px;
    box-shadow: 0 14px 30px rgba(0,0,0,.45);
  }
  .card--front { background: var(--card-black); color: var(--text-white); }
  .card--back { background: var(--brand-green); color: var(--text-white); }

  .wordmark {
    display: flex; align-items: center; gap: 10px;
    font-weight: 700; letter-spacing: 2px; color: var(--text-white);
  }
  .wordmark__square { width: 14px; height: 14px; background: var(--accent-green); }
  .card--back .wordmark__square { background: var(--text-white); }

  .card--front .wordmark { position: absolute; left: 150px; top: 78px; font-size: 28px; }

  .person { position: absolute; left: 60px; top: 198px; }
  .person__name { color: var(--accent-green); font-size: 21px; font-weight: 600; line-height: 1.1; }
  .person__role { font-size: 15px; margin-left: 34px; color: var(--text-soft); }

  .contact-divider {
    position: absolute; left: 300px; top: 150px; width: 1px; height: 70px;
    background: var(--divider);
  }
  .contact { position: absolute; left: 318px; top: 148px; list-style: none; }
  .contact__item {
    display: flex; align-items: center; gap: 12px;
    font-size: 14px; line-height: 23px; color: var(--text-soft);
  }
  .contact__icon { width: 12px; height: 12px; fill: var(--accent-green); flex: none; }
  .social-square {
    position: absolute; left: 322px; top: 240px; width: 22px; height: 22px;
    background: var(--text-white); border-radius: 4px;
  }

  .card--back .wordmark { position: absolute; left: 40px; top: 150px; font-size: 26px; }
  .services { position: absolute; left: 300px; top: 52px; }
  .services__title { font-size: 17px; font-weight: 700; margin-bottom: 8px; }
  .services__list { list-style: none; }
  .services__item { font-size: 13px; line-height: 21px; }
  .services__item:nth-child(2) { padding-left: 14px; }
  .services__item:nth-child(3) { padding-left: 28px; }
  .services__item:nth-child(4) { padding-left: 42px; }
  .services__item:nth-child(5) { padding-left: 56px; }
  .services__item:first-child { padding-left: 18px; }
</style>
</head>
<body>
<main class="canvas">
  <section class="card card--front" aria-label="Business card front">
    <div class="wordmark"><span class="wordmark__square"></span>BRELVAN BUILD</div>

    <div class="contact-divider"></div>
    <ul class="contact">
      <li class="contact__item">
        <svg class="contact__icon" viewBox="0 0 24 24"><path d="M6.6 10.8a15 15 0 0 0 6.6 6.6l2.2-2.2c.3-.3.7-.4 1-.2 1.1.4 2.3.6 3.6.6.6 0 1 .4 1 1V20c0 .6-.4 1-1 1A17 17 0 0 1 3 4c0-.6.4-1 1-1h3.5c.6 0 1 .4 1 1 0 1.3.2 2.5.6 3.6.1.3 0 .7-.2 1z"/></svg>
        (044)-555-0192
      </li>
      <li class="contact__item">
        <svg class="contact__icon" viewBox="0 0 24 24"><path d="M2 5h20v14H2z M2 5l10 8 10-8" stroke="#0d0d0d" stroke-width="1.5"/></svg>
        info@brelvanbuild.com.au
      </li>
      <li class="contact__item">
        <svg class="contact__icon" viewBox="0 0 24 24"><circle cx="12" cy="12" r="10"/></svg>
        brelvanbuild.com.au
      </li>
    </ul>
    <div class="social-square" aria-hidden="true"></div>

    <div class="person">
      <p class="person__name">David Martin</p>
      <p class="person__role">Managing Director</p>
    </div>
  </section>

  <section class="card card--back" aria-label="Business card back">
    <div class="wordmark"><span class="wordmark__square"></span>BRELVAN BUILD</div>
    <div class="services">
      <h2 class="services__title">Services we provide</h2>
      <ul class="services__list">
        <li class="services__item">Renovations</li>
        <li class="services__item">Deckings &amp; Pergolas</li>
        <li class="services__item">Kitchens</li>
        <li class="services__item">Bathrooms</li>
        <li class="services__item">Intricate details</li>
      </ul>
    </div>
  </section>
</main>
</body>
</html>
```